Tesmaro Realty Business Cards

Design business card

Target Market(s)

High-End Buyer of Real Estate over $1 million dollars

Industry/Entity Type

Realtor

Contact Information for Business Card

Lina Tesmaro R(S) LIC.# 41927
Cell 808 555-0163
Email Lina@Tesmaro.net
Website PeakHomeFinds.com

Also Need Cards for:

Glen Tesmaro R(B) LIC# 60418
C 808 555-0192
E Glen@Tesmaro.net
W PeakHomeFinds.com

Colors

Designer to choose colors to be used in the design.

Requirements
Must have
• Address on back:
• 57 Oleander Ct. , Wailea HI 96721
• Logo on back
Nice to have
• I would like the phone numbers and email address to be big so people can read it easily
Should not have
• Very small print Except For: address (57 Oleander Ct. Wailea HI 96721)

```html
<!DOCTYPE html>
<html lang="en">
<head>
<meta charset="utf-8">
<title>Tesmaro Realty Business Cards</title>
<link rel="stylesheet" href="https://fonts.googleapis.com/css2?family=Jost:wght@600&family=Source+Sans+3:wght@400&display=swap">
<style>
  :root {
    --canvas: #ebebed;
    --ink: #0d0d0d;
    --paper: #ffffff;
    --ring: #4a4a4a;
    --photo-light: #e9e6e4;
    --photo-mid: #c9a48f;
  }
  * { margin: 0; padding: 0; box-sizing: border-box; }
  html, body { width: 1200px; height: 1200px; overflow: hidden; background: var(--canvas); }
  .canvas { position: relative; width: 1200px; height: 1200px; }

  .card { position: absolute; border-radius: 32px; overflow: hidden; }
  .card-back { left: 124px; top: 38px; width: 952px; height: 544px; background: var(--ink); }
  .card-front { left: 122px; top: 621px; width: 956px; height: 547px; background: var(--ink); }

  .brand-plate {
    position: absolute; left: 100px; top: 106px; width: 750px; height: 248px;
    background: var(--paper); border-radius: 40px;
    display: flex; align-items: center;
  }
  .brand-square { width: 150px; height: 150px; background: var(--ink); margin-left: 55px; flex: none; }
  .brand-divider { width: 10px; align-self: stretch; background: var(--ink); margin-left: 55px; flex: none; }
  .brand-name {
    font-family: "Jost", sans-serif; font-weight: 600; color: var(--ink);
    margin-left: 40px; line-height: 1.1; font-size: 76px;
  }
  .brand-name span { display: block; }
  .brand-name .line-2 { letter-spacing: 0.32em; }

  .address {
    position: absolute; left: 0; right: 0; top: 396px; text-align: center;
    font-family: "Source Sans 3", sans-serif; font-size: 39px; color: var(--paper);
  }

  .front-left { position: absolute; left: 0; top: 0; width: 478px; height: 100%; background: var(--paper); }
  .stack-logo {
    position: absolute; left: 88px; top: 25px; width: 297px; height: 496px;
    background: var(--ink); border-radius: 22px; overflow: hidden;
  }
  .stack-word {
    position: absolute; left: 0; right: 0; text-align: center;
    font-family: "Jost", sans-serif; font-weight: 600; font-size: 44px; color: var(--paper);
  }
  .stack-word.top { top: 24px; letter-spacing: 0.02em; }
  .stack-word.bottom { bottom: 22px; letter-spacing: 0.3em; padding-left: 0.3em; }
  .stack-rule { position: absolute; left: 0; right: 0; height: 10px; background: var(--paper); }
  .stack-rule.top { top: 96px; }
  .stack-rule.bottom { bottom: 88px; }
  .stack-square {
    position: absolute; left: 78px; top: 188px; width: 140px; height: 140px;
    border: 6px solid var(--paper);
  }

  .portrait {
    position: absolute; left: 596px; top: 69px; width: 220px; height: 220px; border-radius: 50%;
    border: 4px solid var(--ring);
    background: radial-gradient(circle at 50% 70%, var(--photo-mid), var(--photo-light) 70%);
  }
  .agent { position: absolute; left: 572px; top: 311px; color: var(--paper); font-family: "Source Sans 3", sans-serif; }
  .agent-name { font-size: 28px; line-height: 1; }
  .agent-licence { font-size: 19px; margin-top: 6px; }
  .contacts { list-style: none; margin-top: 14px; }
  .contacts li { display: flex; align-items: center; font-size: 25px; height: 37px; letter-spacing: 0.02em; }
  .contacts svg { width: 22px; height: 22px; margin-right: 12px; fill: var(--paper); flex: none; }
</style>
</head>
<body>
<main class="canvas">
  <section class="card card-back" aria-label="Card back">
    <div class="brand-plate">
      <div class="brand-square"></div>
      <div class="brand-divider"></div>
      <div class="brand-name"><span class="line-1">TESMARO</span><span class="line-2">REALTY</span></div>
    </div>
    <p class="address">57 Oleander Ct. , Wailea HI 96721</p>
  </section>

  <section class="card card-front" aria-label="Card front">
    <div class="front-left">
      <div class="stack-logo">
        <div class="stack-word top">TESMARO</div>
        <div class="stack-rule top"></div>
        <div class="stack-square"></div>
        <div class="stack-rule bottom"></div>
        <div class="stack-word bottom">REALTY</div>
      </div>
    </div>
    <div class="portrait" role="img" aria-label="Portrait photo of the two agents"></div>
    <div class="agent">
      <p class="agent-name">Lina Tesmaro R(S)</p>
      <p class="agent-licence">LIC.# 41927</p>
      <ul class="contacts">
        <li><svg viewBox="0 0 24 24" aria-hidden="true"><path d="M6.6 10.8a15.1 15.1 0 0 0 6.6 6.6l2.2-2.2a1 1 0 0 1 1-.25 11.4 11.4 0 0 0 3.6.57 1 1 0 0 1 1 1V20a1 1 0 0 1-1 1A17 17 0 0 1 3 4a1 1 0 0 1 1-1h3.5a1 1 0 0 1 1 1c0 1.25.2 2.45.57 3.57a1 1 0 0 1-.25 1z"/></svg>808 555-0163</li>
        <li><svg viewBox="0 0 24 24" aria-hidden="true"><path d="M2 5h20v14H2z M2 5l10 8 10-8" fill="none" stroke="#fff" stroke-width="0"/><path d="M2 6.5V19h20V6.5l-10 7.5z M2.8 5h18.4L12 11.8z"/></svg>Lina@Tesmaro.net</li>
        <li><svg viewBox="0 0 24 24" aria-hidden="true"><circle cx="12" cy="12" r="10" fill="none" stroke="#fff" stroke-width="2"/><path d="M12 2v20M2 12h20M12 2c-4 5-4 15 0 20M12 2c4 5 4 15 0 20" fill="none" stroke="#fff" stroke-width="1.6"/></svg>PeakHomeFinds.com</li>
      </ul>
    </div>
  </section>
</main>
</body>
</html>
```